Larkmoor Health- Core Values Graphic for Visual Appeal

I would like a poster that could take these written core values from our organization and create a graphic that we could use for our staff and employees. I would also like to incorporate our branding into this project. Thank you!

Target Market(s)

To helps patients and employees understand the core values of our organization

Industry/Entity Type

Healthcare

Requirements
Must have
• Match our branding
Nice to have
• Please use your creativity!
Should not have
• Overly complex/ busy

```html
<!DOCTYPE html>
<html lang="en">
<head>
<meta charset="utf-8">
<title>Larkmoor Health – Core Values</title>
<link rel="stylesheet" href="https://fonts.googleapis.com/css2?family=Ubuntu:wght@400;500;700&display=swap">
<style>
  :root {
    --page: #ffffff;
    --slate: #404042;
    --sky: #29a8e0;
    --sky-deep: #1a7fd0;
    --ink: #2b2b2d;
    --text-light: #ffffff;
    --photo-light: #eef1f4;
    --photo-mid: #c9d6e2;
  }
  * { margin: 0; padding: 0; box-sizing: border-box; }
  html, body { width: 927px; height: 1200px; overflow: hidden; background: var(--page); }
  .poster {
    position: relative;
    width: 927px;
    height: 1200px;
    font-family: "Ubuntu", sans-serif;
    overflow: hidden;
  }
  .poster-art { position: absolute; inset: 0; }
  .brand {
    position: absolute;
    left: 110px;
    top: 118px;
    display: flex;
    align-items: center;
    gap: 10px;
  }
  .brand-dot {
    width: 26px; height: 26px;
    border-radius: 50%;
    background: var(--sky);
  }
  .brand-name {
    font-weight: 700;
    font-size: 28px;
    color: var(--ink);
    letter-spacing: 0.5px;
  }
  .value-text {
    position: absolute;
    left: 146px;
    width: 418px;
    font-size: 10.6px;
    line-height: 15.1px;
    color: var(--text-light);
  }
  .value-label {
    position: absolute;
    left: -10px;
    width: 200px;
    text-align: center;
    font-weight: 700;
    font-size: 19.5px;
    line-height: 22px;
    color: var(--text-light);
  }
  .values-intro {
    position: absolute;
    left: 623px;
    top: 553px;
    width: 262px;
    font-weight: 700;
    font-size: 16.4px;
    line-height: 21.1px;
    color: var(--text-light);
  }
</style>
</head>
<body>
<main class="poster">
  <svg class="poster-art" width="927" height="1200" viewBox="0 0 927 1200">
    <defs>
      <linearGradient id="photoTone" x1="0" y1="0" x2="0" y2="1">
        <stop offset="0" stop-color="#ffffff"/>
        <stop offset="0.55" stop-color="#eef1f4"/>
        <stop offset="1" stop-color="#c9d6e2"/>
      </linearGradient>
      <linearGradient id="waveTone" x1="0" y1="0" x2="0" y2="1">
        <stop offset="0" stop-color="#29a8e0"/>
        <stop offset="0.6" stop-color="#1a7fd0"/>
        <stop offset="1" stop-color="#29a8e0"/>
      </linearGradient>
    </defs>

    <rect class="page" width="927" height="1200" fill="var(--page)"/>

    <rect class="team-photo" x="316" y="78" width="530" height="350" rx="4"
          fill="url(#photoTone)" role="img"
          aria-label="Photo of three clinicians: a man in blue scrubs, a senior doctor in a white coat with a stethoscope and clipboard, and a woman in a white coat"/>

    <path class="slate-field" d="M0,369 Q480,585 927,351 L927,1200 L0,1200 Z" fill="var(--slate)"/>
    <path class="sky-wave" d="M0,199 Q420,550 927,321 L927,351 Q480,585 0,369 Z" fill="url(#waveTone)"/>
    <path class="ink-swoosh" d="M640,385 Q800,355 927,255 L927,288 Q800,375 640,385 Z" fill="#1d1d1f"/>

    <g class="value-tabs" fill="var(--sky)">
      <g transform="translate(0,552)">
        <path d="M0,-40 C15,-26 30,-22 60,-22 L60,22 C30,22 15,26 0,40 Z"/>
        <circle cx="90" cy="0" r="41"/>
      </g>
      <g transform="translate(0,711)">
        <path d="M0,-40 C15,-26 30,-22 60,-22 L60,22 C30,22 15,26 0,40 Z"/>
        <circle cx="90" cy="0" r="41"/>
      </g>
      <g transform="translate(0,870)">
        <path d="M0,-40 C15,-26 30,-22 60,-22 L60,22 C30,22 15,26 0,40 Z"/>
        <circle cx="90" cy="0" r="41"/>
      </g>
      <g transform="translate(0,1029)">
        <path d="M0,-40 C15,-26 30,-22 60,-22 L60,22 C30,22 15,26 0,40 Z"/>
        <circle cx="90" cy="0" r="41"/>
      </g>
    </g>

    <g class="value-icons" fill="#ffffff">
      <g class="icon-family" transform="translate(90,552)">
        <circle cx="-11" cy="-16" r="5"/>
        <circle cx="11" cy="-16" r="5"/>
        <rect x="-19" y="-9" width="15" height="26" rx="5"/>
        <rect x="4" y="-9" width="15" height="26" rx="5"/>
        <circle cx="0" cy="-4" r="4" fill="var(--sky)"/>
        <circle cx="0" cy="-4" r="3.2"/>
        <rect x="-6" y="1" width="12" height="16" rx="4" stroke="var(--sky)" stroke-width="1.5"/>
      </g>
      <g class="icon-excellence" transform="translate(90,711)">
        <polygon points="0,-22 4,-13 13,-12 6,-6 8,3 0,-2 -8,3 -6,-6 -13,-12 -4,-13"/>
        <path d="M-16,-6 L-10,-6 L-10,6 Q0,12 10,6 L10,-6 L16,-6 L16,8 Q8,16 4,16 L4,19 L-4,19 L-4,16 Q-8,16 -16,8 Z"/>
        <rect x="-12" y="20" width="24" height="5" rx="1"/>
      </g>
      <g class="icon-integrity" transform="translate(90,870)">
        <circle r="20"/>
        <path d="M0,-20 L0,20 M-20,0 L20,0" stroke="var(--sky)" stroke-width="2.5"/>
        <circle cx="0" cy="-8" r="3.5" fill="var(--sky)"/>
        <circle cx="8" cy="0" r="3.5" fill="var(--sky)"/>
      </g>
      <g class="icon-service" transform="translate(90,1029)">
        <circle r="17"/>
        <rect x="-4" y="-23" width="8" height="8" rx="1"/>
        <rect x="-4" y="15" width="8" height="8" rx="1"/>
        <rect x="-23" y="-4" width="8" height="8" rx="1"/>
        <rect x="15" y="-4" width="8" height="8" rx="1"/>
        <g transform="rotate(45)">
          <rect x="-4" y="-23" width="8" height="8" rx="1"/>
          <rect x="-4" y="15" width="8" height="8" rx="1"/>
          <rect x="-23" y="-4" width="8" height="8" rx="1"/>
          <rect x="15" y="-4" width="8" height="8" rx="1"/>
        </g>
        <circle r="11" fill="var(--sky)"/>
        <path d="M-7,-10 L-7,-3 Q0,3 7,-3 L7,-10 L3,-10 L3,-5 L-3,-5 L-3,-10 Z M-3,0 L3,0 L3,16 L-3,16 Z"/>
      </g>
    </g>

    <line class="intro-rule" x1="623" y1="742" x2="927" y2="742" stroke="var(--sky)" stroke-width="2"/>
    <circle class="accent-disc" cx="716" cy="933" r="86" fill="var(--sky)"/>

    <path class="white-waves"
          d="M394,1200 C394,1140 424,1093 476,1093 C530,1093 550,1147 593,1147 C640,1147 660,1096 713,1096 C765,1096 790,1147 837,1147 C880,1147 900,1105 927,1099 L927,1200 Z"
          fill="var(--page)"/>
  </svg>

  <div class="brand">
    <span class="brand-dot"></span>
    <span class="brand-name">Larkmoor Health</span>
  </div>

  <p class="value-text" style="top:522px">At the heart of our mission is the commitment to provide high-quality, affordable healthcare in a comforting and uplifting family-oriented environment. Just as our community is our extended family, every patient is a cherished member of our healthcare family. We treat each individual with the same care, compassion, and respect we would offer to our own loved ones.</p>
  <h2 class="value-label" style="top:602px">Family</h2>

  <p class="value-text" style="top:681px">In line with our goal, we aspire not only to alleviate pain but also to inspire patients to become active participants in their well-being. We believe in empowering our patients through education and compassion. Our pursuit of excellence is unwavering, driven by our dedication to continuously improve our services at every level, ensuring that our community receives nothing less than exceptional care.</p>
  <h2 class="value-label" style="top:761px">Excellence</h2>

  <p class="value-text" style="top:839px">In our healthcare team, 'Integrity' is non-negotiable. Our purpose is deeply rooted in ethics, integrity, and professional standards. We operate with the utmost integrity in every aspect of our work, adhering to the highest ethical principles. We understand that trust is the foundation of healthcare, and we are committed to maintaining the trust our community places in us.</p>
  <h2 class="value-label" style="top:920px">Integrity</h2>

  <p class="value-text" style="top:999px">Our vision is grounded in the belief that every person possesses the innate potential for true health. We aim to facilitate the body's natural healing response by providing the highest level of service. Our hope for each patient extends beyond healing; we aspire to help you fulfill your life's mission and purpose abundantly, supporting you in your journey to well-being.</p>
  <h2 class="value-label" style="top:1079px">Service</h2>

  <p class="values-intro">These core values are the spirit of who we are as a healthcare team. They guide our actions, unite us in purpose, and ensure that we provide world-class care while fostering a positive and supportive atmosphere within our team:</p>
</main>
</body>
</html>
```